Bed Company needs business card

Hello, we are a bed company that makes specialized magnets for beds. We are an alternative healing company. I need a modern and upscale business card. Please incorporate my logo for the card.

Accepted file formats are AI, EPS, and Press-Ready PDFS.

Please include all fonts or convert them to outlines regardless of file type.

If you are designing the card in Photoshop the file Must be 1200dpi.

I am open to anything for the business card.  I really like all of your designs and if you want to change the color of the logo, you can.  I will be making the final selection by Friday.  Thank You for all of your designs.  Feel Free to submit different color logos if you want.  

Reason: I will make a decision Final on Friday April 20th. 2012. Good Luck and Thank you all for the designs.

Target Market(s)

My target Market is people, who are looking for alternative healing.

Industry/Entity Type

Business

Requirements
Must have
• My logo must be incorporated. The front card must have

Name
Job Title

Address
Work
Cell
Fax
email
web

Just put in fake info for the card.

The back of the card. I want the logo on the back with color. I just want it to look modern and cool.

```html
<!DOCTYPE html>
<html lang="en">
<head>
<meta charset="utf-8">
<title>Lodestone Rest – Business Cards</title>
<link href="https://fonts.googleapis.com/css2?family=Questrial&display=swap" rel="stylesheet">
<style>
  :root {
    --backdrop: #ecebe8;
    --card: #ffffff;
    --green-deep: #0f5a2a;
    --green-mid: #1f8f34;
    --green-bright: #2cb63c;
    --ink: #1d1d1d;
    --muted: #4a4a4a;
  }
  * { margin: 0; padding: 0; box-sizing: border-box; }
  html, body {
    width: 1200px; height: 900px; overflow: hidden;
    background: var(--backdrop);
    font-family: "Questrial", "Helvetica Neue", Arial, sans-serif;
  }
  .stage {
    position: relative; width: 1200px; height: 900px;
    display: flex; align-items: center; justify-content: center; gap: 40px;
  }
  .card {
    position: relative; width: 530px; height: 300px;
    background: var(--card);
    box-shadow: 0 6px 18px rgba(0,0,0,0.12);
    overflow: hidden;
  }
  .card__band {
    position: absolute; left: 0; top: 0; width: 100%; height: 68px;
    background: linear-gradient(90deg, var(--green-deep), var(--green-bright) 35%, var(--green-mid) 65%, var(--green-bright));
  }
  .brand { display: flex; align-items: center; gap: 14px; }
  .brand__mark { width: 40px; height: 40px; background: var(--green-deep); flex: none; }
  .brand__text { display: flex; flex-direction: column; }
  .brand__name { font-size: 38px; color: var(--green-deep); line-height: 1; }
  .brand__tagline { font-size: 15px; color: var(--green-mid); letter-spacing: 1px; margin-top: 4px; }

  .card--back .brand { position: absolute; left: 62px; top: 150px; }

  .card--front .brand { position: absolute; left: 30px; top: 206px; gap: 10px; }
  .card--front .brand__mark { width: 28px; height: 28px; }
  .card--front .brand__name { font-size: 24px; }
  .card--front .brand__tagline { font-size: 10px; }

  .contact {
    position: absolute; left: 300px; top: 84px; color: var(--ink);
  }
  .contact__name { font-size: 17px; }
  .contact__title { font-size: 17px; margin-bottom: 8px; }
  .contact__list { list-style: none; font-size: 12.5px; color: var(--muted); }
  .contact__list li { display: flex; align-items: center; gap: 7px; line-height: 17px; }
  .contact__icon { width: 9px; height: 9px; flex: none; fill: var(--green-mid); }
  .contact__address { font-size: 13px; color: var(--ink); margin-top: 10px; line-height: 17px; }
</style>
</head>
<body>
<main class="stage">
  <section class="card card--back" aria-label="Card back">
    <div class="card__band" role="img" aria-label="Green geometric triangle pattern band"></div>
    <div class="brand">
      <span class="brand__mark"></span>
      <div class="brand__text">
        <span class="brand__name">Lodestone Rest</span>
        <span class="brand__tagline">Alternative Healing</span>
      </div>
    </div>
  </section>

  <section class="card card--front" aria-label="Card front">
    <div class="card__band" role="img" aria-label="Green geometric triangle pattern band"></div>
    <div class="brand">
      <span class="brand__mark"></span>
      <div class="brand__text">
        <span class="brand__name">Lodestone Rest</span>
        <span class="brand__tagline">Alternative Healing</span>
      </div>
    </div>
    <div class="contact">
      <p class="contact__name">Clara Whitmore</p>
      <p class="contact__title">Director</p>
      <ul class="contact__list">
        <li><svg class="contact__icon" viewBox="0 0 10 10"><path d="M2 0.5 L4 2.5 L3 4 Q4.5 6 6 7 L7.5 6 L9.5 8 L8 9.5 Q3 9 0.5 2 Z"/></svg>8301 4416</li>
        <li><svg class="contact__icon" viewBox="0 0 10 10"><rect x="1" y="3" width="8" height="6" rx="1"/><rect x="3" y="0.5" width="4" height="3"/></svg>8301 4417</li>
        <li><svg class="contact__icon" viewBox="0 0 10 10"><rect x="2.5" y="0" width="5" height="10" rx="1"/></svg>0432 570 218</li>
        <li><svg class="contact__icon" viewBox="0 0 10 10"><rect x="0" y="2" width="10" height="6.5"/></svg>clara@lodestonerest.com</li>
        <li><svg class="contact__icon" viewBox="0 0 10 10"><circle cx="5" cy="5" r="4.5"/></svg>www.lodestonerest.com.au</li>
      </ul>
      <p class="contact__address">14 Larkspur Lane<br>Elmview SA 5999</p>
    </div>
  </section>
</main>
</body>
</html>
```